Organic skincare label - minimalist, earthy, luxe design needed!

I need a label design for a luxury natural skin care line called "Velka Botanix". Velka means 'earth' in Swahili. I would like the design to embody an earthy feel but be minimalistic and give a luxe vibe. My first product will be a Tumeric and Neem Scrub.

The size of the jar is 8oz, label dimensions should be (1.625" Tall x 8.5" Wide)
I will be making other products too such as; oils + toners so I feel free to do labels for glass bottles and/or spray bottles as well.

Forest green, light pinks/nudes/beige, grey, white, gold, are colors that can be used (not all have to be used).

I have included pictures of some things I've worked on myself as well as my original logo design but I need to simplify the logo, no circle around it.
Feel free to get creative.

Thank you! :)
Updates

Target Market(s)

Socially Conscious, Beauty Enthusiast, Minimalist

Industry/Entity Type

Skin Care

Font styles to use
Sans Serif
Other font styles liked:
• "Wonderlove doodle" is the font used for "Velka" in the logo. Feel free to use that or change it as you see fit.

Requirements
Must have
• Simplistic design
would like to stick to a font close to the ones in the logo. Either the one used for the name "Velka" OR the one that the slogan "Nature's Remedies" uses.

I have also included some pictures to capture the aesthetic of my social media and website.

Gender neutral

```html
<!DOCTYPE html>
<html lang="en">
<head>
<meta charset="utf-8">
<title>Velka Botanix – Turmeric + Neem Scrub Label</title>
<link rel="stylesheet" href="https://fonts.googleapis.com/css2?family=Montserrat:wght@400;600;700&display=swap">
<style>
  :root {
    --blush-outer: #fce4f6;
    --blush-panel: #fdc3eb;
    --ink: #000000;
  }
  * { margin: 0; padding: 0; box-sizing: border-box; }
  html, body {
    width: 1200px;
    height: 230px;
    overflow: hidden;
    background: var(--blush-outer);
  }
  .label {
    position: relative;
    width: 1200px;
    height: 230px;
    background: var(--blush-outer);
    font-family: "Montserrat", Arial, sans-serif;
    color: var(--ink);
  }
  .label-panel {
    position: absolute;
    left: 18px;
    top: 18px;
    width: 1164px;
    height: 194px;
    background: var(--blush-panel);
  }
  .brand-name,
  .slogan,
  .product-name {
    position: absolute;
    left: 57px;
    line-height: 1;
    white-space: nowrap;
  }
  .brand-name {
    top: 47px;
    font-weight: 700;
    font-size: 40px;
    letter-spacing: 0.5px;
  }
  .slogan {
    top: 97px;
    font-weight: 400;
    font-size: 30px;
    letter-spacing: 0.5px;
  }
  .product-name {
    top: 151px;
    left: 59px;
    font-weight: 400;
    font-size: 35px;
    letter-spacing: 1px;
  }
  .product-name .plus { font-weight: 600; }
  .ingredients {
    position: absolute;
    right: 40px;
    top: 81px;
    text-align: right;
    font-size: 19px;
    line-height: 23.5px;
    letter-spacing: 0.3px;
    white-space: nowrap;
  }
  .ingredients-title {
    font-weight: 600;
    font-size: 20px;
  }
</style>
</head>
<body>
  <div class="label">
    <div class="label-panel"></div>

    <h1 class="brand-name">VELKA BOTANIX</h1>
    <p class="slogan">NATURE’S REMEDIES</p>
    <p class="product-name">TURMERIC <span class="plus">+</span> NEEM SCRUB</p>

    <div class="ingredients">
      <p class="ingredients-title">INGREDIENTS:</p>
      <p>TURMERIC ROOT, NEEM</p>
      <p>(GROUND LEAVES),</p>
      <p>SUGAR, ESSENTIAL OILS</p>
      <p>(VANILLA, LAVENDER)</p>
    </div>
  </div>
</body>
</html>
```